Swimming Pool Supply Company Business Cards

We need business cards designed for company. These need to be easy to edit so that we can fill in names, titles, and contact info for each person who works here.

Dalton R. Whitfield
Manager of Legal & Finance
K.L. Brisbane, Incorporated

4837 Grenway Avenue
Marlow Heights, PA 19243

E. dalton@klbrisbane-example.com
M. (215) 555-0173
O. (215) 555-0148

Contact Information for Business Card

Looking to upgrade current business cards with graphic that can be edited. Looking for fresh ideas for an age old industry.

Font styles to use
Serif
Sans Serif

Colors

Designer to choose colors to be used in the design.

Requirements
Must have
• Professional, fresh, unique but professional

```html
<!DOCTYPE html>
<html lang="en">
<head>
<meta charset="utf-8">
<title>K.L. Brisbane, Incorporated — Business Card</title>
<link rel="stylesheet" href="https://fonts.googleapis.com/css2?family=Arimo:wght@400&display=swap">
<style>
  :root {
    --backdrop: #c4c3c4;
    --card: #fbfbfb;
    --ink: #5a5a5a;
    --ink-soft: #6a6a6a;
    --brand: #1f5fb8;
  }
  * { box-sizing: border-box; margin: 0; padding: 0; }
  html, body { width: 1200px; height: 960px; overflow: hidden; }
  body {
    background: var(--backdrop);
    font-family: "Arimo", Arial, sans-serif;
    color: var(--ink);
    position: relative;
  }
  .card {
    position: absolute;
    left: 250px;
    width: 700px;
    height: 400px;
    background: var(--card);
    box-shadow: 0 2px 6px rgba(0,0,0,0.12);
  }
  .card--front { top: 40px; }
  .card--back { top: 480px; display: flex; align-items: center; justify-content: center; }

  .person { position: absolute; left: 360px; top: 88px; }
  .person__name { font-size: 27px; color: var(--ink); letter-spacing: 0.2px; }
  .person__title { font-size: 17px; color: var(--ink-soft); margin-top: 4px; margin-left: 8px; }

  .brand { position: absolute; right: 48px; top: 232px; text-align: right; }
  .brand__mark { display: flex; align-items: center; justify-content: flex-end; gap: 12px; }
  .brand__dot { width: 22px; height: 22px; border-radius: 50%; background: var(--brand); }
  .brand__word { font-size: 42px; color: var(--brand); letter-spacing: 2px; line-height: 1; }
  .brand__company { font-size: 19px; color: var(--brand); margin-top: 14px; }

  .contact { position: absolute; left: 48px; top: 250px; font-size: 17px; line-height: 1.35; color: var(--ink); }
  .contact__lines { margin-top: 14px; }

  .tagline { font-size: 24px; color: var(--ink); letter-spacing: 0.2px; }
</style>
</head>
<body>
  <section class="card card--front">
    <div class="person">
      <p class="person__name">Dalton R. Whitfield</p>
      <p class="person__title">Manager of Legal &amp; Finance</p>
    </div>

    <div class="contact">
      <p>4837 Grenway Avenue<br>Marlow Heights, PA 19243</p>
      <p class="contact__lines">E. dalton@klbrisbane-example.com<br>M. (215) 555-0173<br>O. (215) 555-0148</p>
    </div>

    <div class="brand">
      <div class="brand__mark">
        <span class="brand__dot"></span>
        <span class="brand__word">BRISBANE</span>
      </div>
      <p class="brand__company">K.L. Brisbane, Incorporated</p>
    </div>
  </section>

  <section class="card card--back">
    <p class="tagline">Swimming Pools, Supplies, and Accessories</p>
  </section>
</body>
</html>
```